London based Blowdry bar needs drinks menu

Volara Blowdry Bar is a successful trendy 'Blowdry bar' based in London. We offer our clients a number of services that are quick, affordable and ideal for a perfect night out!
Within the salon we offer soft & alcoholic drinks - I need to advertise this but space is limited. Therefore I would like to have a simple but pretty bar menu that will be designed like a banner and run under the mirrors at each position.
Please look at our website to have a look inside salon and pick up design ideas, colours used and feel of salon.
Website = www.quickstylelounge.co.uk
Font used for Volara logo = Houschka rounded
Font used on website = District Pro
Measurement for each menu 90cm length x 7.5cm height (horizontal menu)
Target Market(s)
20-50 year olds - clients in salon to have a fast fun experience. needs to be clear, easy to read and to the point
Font styles to use
Other font styles liked:
- District Pro
Requirements
Must have
- Title of drink, price of drink - easy to read font
Nice to have
- Nice to have a picture of drink in beginning of menu (nice visual add) to draw attention to clients eyes and so they understand it is a drinks menu. Clear points at the beginning of each drink.

```html
<!DOCTYPE html>
<html lang="en">
<head>
<meta charset="utf-8">
<title>Volara Blowdry Bar – Drinks Menu Banner</title>
<link rel="stylesheet" href="https://fonts.googleapis.com/css2?family=Montserrat:wght@800&family=Open+Sans:ital,wght@0,700;1,700&display=swap">
<style>
  :root {
    --ink: #111111;
    --lime: #c6de86;
    --pink: #e2509b;
    --white: #ffffff;
    --text: #1d1d1b;
    --wash-a: #fbe3ee;
    --wash-b: #fff6e0;
    --wash-c: #e6f3e8;
  }
  * { box-sizing: border-box; margin: 0; padding: 0; }
  html, body { width: 1200px; height: 100px; overflow: hidden; background: var(--white); }
  .banner {
    position: relative;
    width: 1200px;
    height: 100px;
    overflow: hidden;
    font-family: "Open Sans", Arial, sans-serif;
  }
  .banner__backdrop { position: absolute; inset: 0; }
  .brand {
    position: absolute;
    left: 10px; top: 40px;
    width: 86px;
    text-align: center;
    color: var(--white);
    font-family: "Open Sans", Arial, sans-serif;
    font-weight: 700;
    font-size: 14px;
    line-height: 20px;
    letter-spacing: 1px;
  }
  .headline {
    position: absolute;
    left: 112px; top: 7px;
    font-family: "Montserrat", Arial, sans-serif;
    font-weight: 800;
    text-transform: uppercase;
    line-height: 1;
  }
  .headline__top { display: block; color: var(--white); font-size: 40px; letter-spacing: 0.5px; }
  .headline__bottom { display: block; color: var(--lime); font-size: 53px; margin-top: 2px; letter-spacing: 1px; }
  .headline__mark { color: var(--pink); }
  .drink-visual {
    position: absolute;
    left: 474px; top: 10px;
    width: 70px; height: 84px;
    border-radius: 50% 50% 10px 10px / 35% 35% 10px 10px;
    background: radial-gradient(ellipse at 50% 25%, #d6ea9c 0%, #eef6d8 55%, rgba(255,255,255,0) 80%);
  }
  .menu-box {
    position: absolute;
    top: 6px; height: 88px;
    border: 3px solid var(--pink);
    background: rgba(255,255,255,0.55);
    list-style: none;
    padding: 5px 8px;
    display: flex; flex-direction: column; justify-content: space-between;
  }
  .menu-box--soft { left: 552px; width: 230px; }
  .menu-box--bar { left: 789px; width: 212px; padding: 4px 6px; }
  .menu-item {
    position: relative;
    padding-left: 20px;
    color: var(--text);
    font-style: italic;
    font-weight: 700;
    font-size: 15px;
    line-height: 1.1;
    white-space: nowrap;
  }
  .menu-box--bar .menu-item { font-size: 12.5px; padding-left: 18px; }
  .menu-item::before {
    content: "";
    position: absolute;
    left: 1px; top: 3px;
    width: 11px; height: 11px;
    border: 2px solid var(--pink);
    border-radius: 50%;
    background: var(--white);
  }
  .menu-box--bar .menu-item::before { width: 10px; height: 10px; top: 2px; }
  .menu-item--plain::before { display: none; }
  .offer-note {
    position: absolute;
    left: 1008px; top: 9px;
    width: 186px;
    color: var(--pink);
    font-family: "Open Sans", Arial, sans-serif;
    font-weight: 700;
    font-size: 15px;
    line-height: 19px;
    text-align: center;
    text-transform: uppercase;
  }
</style>
</head>
<body>
<div class="banner">
  <svg class="banner__backdrop" width="1200" height="100" viewBox="0 0 1200 100" aria-hidden="true">
    <defs>
      <linearGradient id="wash" x1="0" y1="0" x2="1" y2="1">
        <stop offset="0" stop-color="#fff6e0"/>
        <stop offset="0.4" stop-color="#fbe3ee"/>
        <stop offset="0.7" stop-color="#e6f3e8"/>
        <stop offset="1" stop-color="#fbe3ee"/>
      </linearGradient>
    </defs>
    <rect class="backdrop__wash" x="0" y="0" width="1200" height="100" fill="url(#wash)"/>
    <path class="backdrop__accent" d="M0,0 H448 C476,30 428,66 472,100 H0 Z" fill="#c6de86"/>
    <path class="backdrop__panel" d="M0,0 H420 C448,28 402,64 442,100 H0 Z" fill="#111111"/>
  </svg>

  <div class="brand">VOLARA</div>

  <h1 class="headline">
    <span class="headline__top">Why not have</span>
    <span class="headline__bottom">A drink<span class="headline__mark">?</span></span>
  </h1>

  <div class="drink-visual" role="img" aria-label="Illustration of a lime margarita cocktail glass"></div>

  <ul class="menu-box menu-box--soft">
    <li class="menu-item">Filtered Water</li>
    <li class="menu-item">Sparkling Water&nbsp; £1.50</li>
    <li class="menu-item">Cola / Diet Cola £2</li>
    <li class="menu-item">100% real Fruit Juice £2</li>
  </ul>

  <ul class="menu-box menu-box--bar">
    <li class="menu-item">Dry White Wine / Red Wine £4</li>
    <li class="menu-item">Prosecco / Rose Prosecco £5</li>
    <li class="menu-item">Prosecco Cocktails</li>
    <li class="menu-item menu-item--plain">Choose from Elderflower, Peach,</li>
    <li class="menu-item menu-item--plain">Spritz &amp; Hibiscus – £7</li>
  </ul>

  <p class="offer-note">Check out<br>bar board<br>for drink<br>offers...</p>
</div>
</body>
</html>
```